New Web Design Project for Ridgewell Staffing Partners

We need someone who is experienced in Wordpress to create a new modern professional design for our Recruitment Business, Ridgewell Staffing Partners. We need an EXCITING LANDING PAGE, and another 5-6 (refer attached for the contents) pages and The Designer MUST be able to help us publish the web pages on our server, Hostivra, when completed. This Project is urgent and we require someone who can provide a Fast Turnaround time within 3days. Please refer attached Logo, Brochure, Banner and Name Cards to create the same design branding. Attached also the colour code and font typesLANDING PAGEWHY USSERVICES- RECRUITMENT SERVICES- PRE-EMPLOYMENT PROGRAMEMPLOYER PAGEAI FOR EMPLOYERS
Updates

Rebranding our logo and colour scheme. Awaiting new logo to be used in the website design

Target Market(s)

Large corporations that recruit high volume low skilled labour intensive workers like cleaners, food process workers, baggage handlers, etc

Industry/Entity Type

Recruitment

Coding

Coded - Design and coding required

Number of Pages Required

5+ page

Colors
ec1f27
0255a3

Requirements
Must have
• It must reflect the same design branding as our attached logo, banner, brochure etc. The colour code and fonts are attached in the Word document. Designer must be able to publish the completed Project in Wordpress on Hostivra, our server. It must use some of our corporate photos which we will email the Designer who won our project. The website must reflect a professional, modern, unique and exciting concept, with the website contents from the attached word document.
Nice to have
• We would like to use photos from our collection and will email to the Designer who won the Project, meanwhile the designer can use stock photos on labour intensive jobs eg Aircraft Cabin cleaners, food processing, aircraft bagge handlers, etc
Should not have
• Not similar to other recruitment websites

```html
<!DOCTYPE html>
<html lang="en">
<head>
<meta charset="utf-8">
<title>Ridgewell Staffing Partners – Recruitment Agency</title>
<link href="https://fonts.googleapis.com/css2?family=Montserrat:wght@500;600;700;800&family=Arimo:wght@400;600;700&display=swap" rel="stylesheet">
<style>
:root{
  --red:#b3102a;
  --red-bright:#ec1f27;
  --blue:#2a5ca8;
  --navy:#1d2b66;
  --ink:#2b2b2b;
  --muted:#4a4a4a;
  --light:#e9e9e9;
  --dark:#1c1c1c;
  --footer:#202020;
  --footer-text:#e6e6e6;
  --white:#ffffff;
}
*{box-sizing:border-box;margin:0;padding:0}
html,body{width:1200px;height:3416px;overflow:hidden}
body{position:relative;font-family:"Arimo",Arial,sans-serif;color:var(--ink);background:var(--light)}
.abs{position:absolute}
.heading{font-family:"Montserrat",Arial,sans-serif;font-weight:800;text-transform:uppercase}
.btn{position:absolute;display:flex;align-items:center;justify-content:center;gap:10px;background:var(--red);color:var(--white);font-family:"Montserrat",Arial,sans-serif;font-weight:700;font-size:18px;text-transform:uppercase;border-radius:26px;height:50px}
.btn .dot{width:18px;height:18px;border-radius:50%;background:var(--white);display:flex;align-items:center;justify-content:center}

/* header */
.topbar{left:0;top:0;width:1200px;height:137px;background:var(--white)}
.brand{left:108px;top:34px;display:flex;align-items:center;gap:12px;font-family:"Montserrat",Arial,sans-serif;font-weight:700;font-size:20px;color:var(--red);line-height:1.1}
.brand .mark{width:28px;height:28px;border-radius:50%;background:var(--red);flex:none}
.info{top:46px;display:flex;gap:14px;align-items:flex-start;font-size:15px;color:var(--ink)}
.info .value{font-weight:600;font-size:15px}
.navbar{left:0;top:137px;width:1200px;height:68px;background:#ececec;border-top:1px solid #ddd;display:flex;justify-content:center;align-items:center;gap:38px;font-size:16px;color:var(--ink)}

/* hero */
.hero{left:0;top:205px;width:1200px;height:625px;overflow:hidden}
.hero-photo{position:absolute;inset:0;background:linear-gradient(180deg,#7a8a90 0%,#4e4e52 45%,#2e2c30 100%)}
.hero-title{left:0;top:440px;width:1200px;text-align:center;color:var(--white);font-size:38px;line-height:56px;letter-spacing:1px;font-weight:700}

/* talent */
.circle-photo{border-radius:50%;border:8px solid var(--white);box-shadow:-8px 0 0 var(--red)}
.talent-title{left:517px;top:963px;color:var(--blue);font-size:37px;line-height:46px}
.bullets{left:519px;top:1064px;width:600px;list-style:none;font-size:14.5px;line-height:30px;color:var(--muted)}
.bullets li{position:relative;padding-left:27px}
.bullets li::before{content:"";position:absolute;left:0;top:8px;width:14px;height:14px;border-radius:50%;background:var(--red)}

/* solutions */
.dark{left:0;top:1480px;width:1200px;height:690px;background:var(--dark)}
.sol-title{left:0;top:1622px;width:1200px;text-align:center;color:var(--white);font-size:34px;line-height:46px}
.sol-text{left:160px;top:1722px;width:880px;text-align:center;color:#e6e6e6;font-size:15.5px;line-height:31.5px}
.card{top:1962px;width:319px;height:270px;background:var(--white);box-shadow:0 2px 8px rgba(0,0,0,.25);text-align:center;padding-top:22px}
.card .icon{width:68px;height:62px;margin:0 auto 16px;border-radius:6px}
.card h3{font-family:"Montserrat",Arial,sans-serif;font-weight:700;font-size:17px;color:var(--navy);text-transform:uppercase;line-height:21px;margin-bottom:14px}
.card p{font-size:13.5px;line-height:26px;color:var(--muted);padding:0 28px}
.card .more{font-size:13px;color:var(--red);margin-top:6px}
.arrow{top:2070px}

/* contact */
.contact-title{left:91px;top:2356px;color:var(--blue);font-size:37px;line-height:46px}
.contact-text{left:91px;top:2455px;width:620px;font-size:15.5px;line-height:31px;color:var(--muted);text-align:justify}

/* footer */
.footer{left:0;top:2983px;width:1200px;height:376px;background:var(--footer)}
.foot-h{font-family:"Montserrat",Arial,sans-serif;font-weight:700;font-size:19px;color:var(--white);text-transform:uppercase;letter-spacing:.5px}
.foot-brand{left:130px;top:3130px;font-family:"Montserrat",Arial,sans-serif;font-weight:700;font-size:18px;color:var(--red-bright)}
.socials{left:102px;top:3210px;display:flex;gap:10px}
.socials span{width:30px;height:30px;border-radius:50%;border:2px solid #ddd}
.foot-contact{left:307px;top:3130px;width:270px;font-size:14px;line-height:24px;list-style:none;color:var(--footer-text)}
.foot-contact li{position:relative;padding-left:26px;margin-bottom:14px}
.foot-contact svg{position:absolute;left:0;top:4px}
.news-text{left:594px;top:3130px;width:320px;font-size:14px;line-height:24px;color:var(--footer-text)}
.news-input{left:594px;top:3196px;width:310px;height:44px;background:var(--white);color:#777;font-size:12px;padding:14px 16px}
.news-btn{left:594px;top:3260px;width:128px;height:40px;background:var(--red);color:var(--white);font-family:"Montserrat",Arial,sans-serif;font-weight:700;font-size:15px;display:flex;align-items:center;justify-content:center}
.links{left:952px;top:3130px;list-style:none;font-size:13px;line-height:25px;color:var(--footer-text)}
.links li::before{content:"";display:inline-block;border-left:6px solid #ddd;border-top:4px solid transparent;border-bottom:4px solid transparent;margin-right:12px}
.copyright{left:0;top:3359px;width:1200px;height:57px;background:#161616;border-top:1px solid #333;color:var(--footer-text);font-size:14px;display:flex;align-items:center;justify-content:center}
</style>
</head>
<body>

<header class="abs topbar">
  <div class="abs brand"><span class="mark"></span><span>Ridgewell<br>Staffing Partners</span></div>
  <div class="abs info" style="left:372px">
    <svg width="30" height="30" viewBox="0 0 30 30"><circle cx="15" cy="15" r="15" fill="var(--red)"/><path d="M10 8c1.5 0 2.5 3 2 4l-1.5 1c1 2.5 3 4.5 5.5 5.5l1-1.5c1-.5 4 .5 4 2 0 1.5-1.5 3-3 3-5 0-11-6-11-11 0-1.5 1.5-3 3-3z" fill="#fff"/></svg>
    <div><div>Need Help? Call us</div><div class="value">210 648 2290</div></div>
  </div>
  <div class="abs info" style="left:582px">
    <svg width="32" height="32" viewBox="0 0 32 32"><circle cx="16" cy="16" r="13" fill="none" stroke="var(--red)" stroke-width="3"/><path d="M16 9v7l5 3" fill="none" stroke="var(--red)" stroke-width="3"/></svg>
    <div><div>Monday – Friday</div><div class="value">6.00 am to 9.00 pm</div></div>
  </div>
  <div class="abs info" style="left:813px">
    <svg width="42" height="32" viewBox="0 0 42 32"><rect x="2" y="4" width="38" height="26" fill="none" stroke="var(--red)" stroke-width="2.5"/><path d="M2 4l19 15 19-15" fill="none" stroke="var(--red)" stroke-width="2.5"/></svg>
    <div><div>Mail us:</div><div class="value">enquiries@ridgewellstaffing.com.au</div></div>
  </div>
</header>

<nav class="abs navbar">
  <span>Home</span><span>Why Us</span><span>Services</span><span>Recruitment Services</span><span>Pre-Employment Program</span><span>Employer Page</span><span>AI For Employers</span>
</nav>

<section class="abs hero">
  <div class="hero-photo" role="img" aria-label="Team photograph of the recruitment staff standing together outdoors"></div>
  <svg class="abs" style="left:0;top:500px" width="1200" height="125" viewBox="0 0 1200 125">
    <path d="M0 30 Q600 150 1200 30 L1200 125 L0 125Z" fill="var(--light)"/>
    <path d="M0 18 Q600 138 1200 18" fill="none" stroke="var(--red)" stroke-width="8"/>
    <path d="M0 30 Q600 155 1200 30" fill="none" stroke="var(--navy)" stroke-width="7"/>
  </svg>
</section>
<h1 class="abs heading hero-title">Ridgewell Staffing Partners – Australia’s<br>Premier Recruitment Agency</h1>
<div class="btn" style="left:498px;top:576px;width:204px">
  <svg width="18" height="18" viewBox="0 0 18 18"><path d="M17 1L1 8l6 2 2 6z" fill="#fff"/></svg>Contact Us
</div>

<div class="abs circle-photo" style="left:95px;top:966px;width:394px;height:394px;background:linear-gradient(160deg,#8d8f8a,#5a5b56 60%,#3f403c)" role="img" aria-label="Workers in high visibility vests handling goods in a warehouse"></div>
<h2 class="abs heading talent-title">Modern Solutions to<br>Sourcing Talent</h2>
<ul class="abs bullets">
  <li>Are you spending exorbitant fees on the generic services of labour hire and direct recruiting companies without seeing results?</li>
  <li>Are your HR support costs increasing alongside growing employee numbers, whilst efficiency decreases?</li>
  <li>Have you wasted valuable time labouring through job advertising, resumes, screenings, interviews, and inductions, yet failing to source high calibre candidates?</li>
  <li>Is your attrition rate exceptionally high?</li>
</ul>
<div class="btn" style="left:519px;top:1303px;width:190px">Read More <span class="dot"><svg width="8" height="10" viewBox="0 0 8 10"><path d="M1 0l6 5-6 5z" fill="var(--red)"/></svg></span></div>

<section class="abs dark"></section>
<svg class="abs" style="left:0;top:1476px" width="1200" height="40" viewBox="0 0 1200 40">
  <path d="M0 0 Q300 -6 600 14 Q900 34 1200 18 L1200 40 L0 40Z" fill="var(--red)"/>
  <path d="M0 10 Q300 4 600 24 Q900 42 1200 28 L1200 40 L0 40Z" fill="var(--dark)"/>
</svg>
<h2 class="abs heading sol-title">Modern Recruitment Solutions for<br>Contemporary Companies</h2>
<p class="abs sol-text">To help your business stay ahead in a modern market, Ridgewell Staffing Partners has cultivated a comprehensive proprietary 7-Step Recruitment Process that actively works to remove unsuitable candidates and bring to the forefront the right applicants to benefit your operations. Our agile, determined and accessible team implement this alongside your management and HR departments to ensure our partnership remains fruitful. By adopting Ridgewell’s methodology, we are proven to be the faster, more reliable, and more cost efficient avenue to sourcing new employees for your company – as opposed to conducting the interviews yourself or outsourcing to a labour-hire company – reducing comparative recruitment costs by up to 75%.</p>

<svg class="abs arrow" style="left:40px" width="36" height="24" viewBox="0 0 36 24"><path d="M34 12H4M14 2L3 12l11 10" fill="none" stroke="#fff" stroke-width="2.5"/></svg>
<svg class="abs arrow" style="left:1124px" width="36" height="24" viewBox="0 0 36 24"><path d="M2 12h30M22 2l11 10-11 10" fill="none" stroke="#fff" stroke-width="2.5"/></svg>

<article class="abs card" style="left:91px">
  <div class="icon" style="background:linear-gradient(#f2c9a0,#3d6fb6)" role="img" aria-label="Icon of a support staff member"></div>
  <h3>Always Available</h3>
  <p>We provide 24/7 ongoing support to all our employer clients nationally and 6 months support to your new staff hired</p>
  <div class="more">Read More →</div>
</article>
<article class="abs card" style="left:440px;padding-top:16px">
  <div class="icon" style="background:linear-gradient(#f5b93a,#d9761e)" role="img" aria-label="Icon of a wallet with coins"></div>
  <h3>Reduce Your<br>Operational Cost</h3>
  <p>Reduce your operating expenses using Ridgewell’s bespoke Pre-Employment Programs to flatline recruitment costs</p>
  <div class="more">Read More →</div>
</article>
<article class="abs card" style="left:790px">
  <div class="icon" style="background:linear-gradient(#8fd3f5,#2f8fd6)" role="img" aria-label="Icon of connected technology devices"></div>
  <h3>Technology</h3>
  <p>We embrace new technology and business automation in supporting various service delivery model to deliver amazing client</p>
  <div class="more">Read More →</div>
</article>

<h2 class="abs heading contact-title">Contact Our Recruitment<br>Specialists Today</h2>
<p class="abs contact-text">We operate throughout Sydney, Melbourne, Brisbane, Adelaide, Perth, Hobart and wider Australia. With our continued growth, we will continue to expand our services globally to accommodate companies across Asia Pacific countries. If you would like to learn more about our services, or request customer testimonials, our team would be happy to oblige. Call us today on +61 3 9000 4821, send an email to enquiries@ridgewellstaffing.com.au, or complete our simple online enquiry form on our contact page to book a 2 hour, obligation free consultation with our professional staff.</p>
<div class="btn" style="left:91px;top:2698px;width:194px">Contact Us <span class="dot"><svg width="8" height="10" viewBox="0 0 8 10"><path d="M1 0l6 5-6 5z" fill="var(--red)"/></svg></span></div>
<div class="abs" style="left:729px;top:2334px;width:398px;height:421px;border-radius:50%;background:var(--red)"></div>
<div class="abs" style="left:743px;top:2342px;width:380px;height:405px;border-radius:50%;border:6px solid var(--white);background:linear-gradient(180deg,#d9d6d0 0%,#c4c0b8 55%,#4a4a4e 100%)" role="img" aria-label="Recruitment specialist working at a desk in the office"></div>

<svg class="abs" style="left:0;top:2875px" width="1200" height="110" viewBox="0 0 1200 110">
  <path d="M0 110 Q600 -40 1200 110Z" fill="var(--footer)"/>
  <path d="M0 104 Q600 -50 1200 104" fill="none" stroke="var(--red)" stroke-width="6"/>
  <path d="M0 94 Q600 -62 1200 94" fill="none" stroke="var(--navy)" stroke-width="6"/>
</svg>
<footer class="abs footer"></footer>
<div class="abs foot-brand" style="display:flex;align-items:center;gap:8px"><span style="width:18px;height:18px;border-radius:50%;background:var(--red-bright)"></span>Ridgewell</div>
<div class="abs socials"><span></span><span></span><span></span><span></span></div>

<h4 class="abs foot-h" style="left:307px;top:3082px">Contact Us</h4>
<ul class="abs foot-contact">
  <li><svg width="14" height="18" viewBox="0 0 14 18"><path d="M7 0a7 7 0 0 1 7 7c0 5-7 11-7 11S0 12 0 7a7 7 0 0 1 7-7z" fill="#ddd"/><circle cx="7" cy="7" r="2.5" fill="var(--footer)"/></svg>Suite 410, Level 12, Harbour Point<br>Tower Two, 58 Lantern Street<br>Melbourne VIC 3005</li>
  <li><svg width="16" height="16" viewBox="0 0 16 16"><path d="M3 1c1.5 0 2.5 3 2 4l-1.2 1c1 2 2.5 3.5 4.5 4.5l1-1.2c1-.5 4 .5 4 2 0 1.5-1.5 3-3 3C6 14 1 9 1 4c0-1.5 .5-3 2-3z" fill="#ddd"/></svg>Phone: +61 3 9000 4821</li>
  <li><svg width="16" height="12" viewBox="0 0 16 12"><rect width="16" height="12" fill="#ddd"/><path d="M0 0l8 6 8-6" fill="none" stroke="var(--footer)" stroke-width="1.5"/></svg>Email: enquiries@ridgewellstaffing.com.au</li>
</ul>

<h4 class="abs foot-h" style="left:594px;top:3082px">Sign Up for Newsletter</h4>
<p class="abs news-text">At vero eos et accusamus et iusto odio dignissimos ducimus quos dolores</p>
<div class="abs news-input">Enter email</div>
<div class="abs news-btn">SIGN UP</div>

<h4 class="abs foot-h" style="left:952px;top:3082px">Quick Links</h4>
<ul class="abs links">
  <li>Home</li><li>Why Us</li><li>Services</li><li>Recruitment Services</li><li>Pre-Employment Program</li><li>Employer Page</li><li>AI For Employers</li>
</ul>

<div class="abs copyright">Copyrights © 2019 All Rights Reserved</div>

</body>
</html>
```